Tour operator needs simple coded WordPress site (updated extra payment for coding and guaranteed)

[update 9/7/2015]
If you design a new logo and it gets accepted, even if we use another template with your logo you will get $50
[update 8/7/2015]
Update on questions about dual-language
For dual languages we are happy to set up a second site with the same designs in a second language.
For the design aspect just allow the user to switch between languages with an icon.
For the coding, a replica of the site on a second server will do (to save messing around with multiple language plugins) - we will populate it with Chinese text
[original post]
Simple coded WordPress site for tours
You can choose to design only or design and code ($340 design, $150 bonus for coding)
Open design brief - use your creativity
Will be in 2 languages (English and Chinese) but design needs only to be in one language
Winning design will be chosen only from home page, but the winner must make a second standard template page when chosen at no extra cost.
Must be responsive design
We only need homepage and standard template page design and coding, we will populate the pages
You can use design ideas from our pamphlet if you like - attached
Only a sample logo and colors on website and pamphlet - feel free to change as the current ones seem restrictive
Current website framework only to give an idea of the number of pages and basic menu structure (no need to use existing navigation style or any style at all for that matter, open brief)
http://brightwaterlearningtrips.com.au/
Target Market(s)
Chinese parents of kids 10-14 (the kids will take the tour)
Industry/Entity Type
Tour
Number of Pages Required
2 page
Look and feel
Each slider illustrates characteristics of the customer's brand and the style your logo design should communicate.

```html
<!DOCTYPE html>
<html lang="en">
<head>
<meta charset="utf-8">
<title>Brightwater Learning Trips</title>
<link href="https://fonts.googleapis.com/css2?family=Oxygen:wght@400;700&family=Roboto:wght@500;700&display=swap" rel="stylesheet">
<style>
:root{
  --navy:#2f3f7f;
  --navy-dark:#243266;
  --gold:#f2b01e;
  --ink:#222;
  --muted:#444;
  --white:#fff;
  --btn:#333;
}
*{box-sizing:border-box;margin:0;padding:0}
html,body{width:1200px;height:1048px;overflow:hidden;background:var(--white)}
body{font-family:'Oxygen',sans-serif;color:var(--ink);position:relative}
.header{position:absolute;top:0;left:0;width:1200px;height:95px;background:var(--white)}
.lang-switch{position:absolute;left:159px;top:23px;width:119px;height:35px;background:#2b2b2b;border-radius:4px;color:#fff;font-size:13px;display:flex;align-items:center;padding-left:18px;gap:8px}
.lang-switch .flag{width:20px;height:13px;background:#4a5a9a;border-radius:1px}
.book-now{position:absolute;left:950px;top:21px;width:89px;height:32px;background:var(--gold);color:#fff;font-family:'Roboto',sans-serif;font-weight:500;font-size:14px;display:flex;align-items:center;justify-content:center;border-radius:2px}
.nav{position:absolute;top:95px;left:0;width:1200px;height:42px;background:var(--navy)}
.nav a{position:absolute;top:0;height:42px;display:flex;align-items:center;justify-content:center;color:#fff;text-decoration:none;font-family:'Roboto',sans-serif;font-weight:500;font-size:15px;border-right:1px solid rgba(255,255,255,.15)}
.nav a.active{border-bottom:3px solid var(--gold)}
.brand{position:absolute;left:510px;top:10px;width:180px;height:180px;border-radius:50%;background:var(--white);border:5px solid var(--navy);box-shadow:0 0 0 4px #fff,0 0 0 6px var(--gold);display:flex;align-items:center;justify-content:center;text-align:center;z-index:3;color:var(--navy);font-family:'Roboto',sans-serif;font-weight:700;font-size:19px;line-height:1.15}
.hero{position:absolute;top:137px;left:0;width:1200px;height:419px;background:linear-gradient(180deg,#9fb8c8 0%,#d9a85a 30%,#c7771c 55%,#6b3a12 80%,#8a5420 100%)}
.hero-title{position:absolute;left:160px;top:286px;color:#fff;font-family:'Roboto',sans-serif;font-weight:500;font-size:26px;line-height:34px;text-shadow:0 2px 3px rgba(0,0,0,.5)}
.hero svg{position:absolute;top:210px}
.features{position:absolute;top:524px;left:0;width:1200px}
.feature{position:absolute;width:260px;text-align:center}
.feature .halo{margin:0 auto;width:150px;height:150px;border-radius:50%;background:var(--white);display:flex;align-items:flex-start;justify-content:center;padding-top:10px}
.feature .badge{width:120px;height:120px;border-radius:50%;display:flex;align-items:center;justify-content:center}
.feature .badge.navy{background:var(--navy);box-shadow:0 0 0 3px #fff,0 0 0 5px var(--navy)}
.feature .badge.gold{background:var(--gold);box-shadow:0 0 0 3px #fff,0 0 0 5px var(--gold)}
.feature h3{margin-top:-4px;font-size:16px;font-weight:700;color:var(--ink)}
.feature h3.highlight{color:var(--navy)}
.divider{position:absolute;top:719px;left:130px;width:940px;height:2px;background:linear-gradient(90deg,transparent,#bbb 15%,#bbb 85%,transparent)}
.about{position:absolute;top:760px;left:0;width:1200px;text-align:center;background:linear-gradient(180deg,#fff,#f4f4f4);height:246px}
.about h2{font-family:'Roboto',sans-serif;font-weight:500;font-size:28px;color:var(--navy);margin-top:6px}
.about h2 .gold{color:var(--gold)}
.ornament{margin:8px auto 0;width:640px;height:14px;position:relative}
.ornament::before{content:"";position:absolute;left:0;right:0;top:6px;height:1px;background:linear-gradient(90deg,transparent,#bbb 30%,#bbb 70%,transparent)}
.ornament span{position:absolute;left:311px;top:-2px;width:18px;height:18px;border-radius:50%;background:var(--gold);border:4px solid var(--navy)}
.about .lead{margin:16px auto 0;width:860px;font-size:13px;font-weight:700;line-height:19px;color:var(--ink)}
.about .body{margin:10px auto 0;width:850px;font-size:13px;line-height:19px;color:var(--muted)}
.read-more{display:inline-block;margin-top:17px;width:105px;height:33px;line-height:33px;background:var(--btn);color:#fff;font-size:14px;border-radius:3px}
.footer{position:absolute;top:1006px;left:0;width:1200px;height:42px;background:var(--navy);color:#fff;font-size:12px}
.footer p{position:absolute;left:160px;top:14px}
.social{position:absolute;left:907px;top:1px;display:flex;gap:7px}
.social span{width:39px;height:39px;border-radius:50%;background:#d8dbe6;border:3px solid #fff;box-shadow:0 0 0 1px #8891b5}
</style>
</head>
<body>
<header class="header">
  <div class="lang-switch"><span class="flag"></span>English
    <svg width="10" height="7" viewBox="0 0 10 7"><path d="M1 1l4 4 4-4" stroke="#fff" stroke-width="1.6" fill="none"/></svg>
  </div>
  <div class="brand">Brightwater<br>Learning<br>Trips</div>
  <a class="book-now">Book Now</a>
</header>
<nav class="nav">
  <a class="active" style="left:160px;width:140px">HOME</a>
  <a style="left:300px;width:149px">TOURS</a>
  <a style="left:751px;width:155px;border-left:1px solid rgba(255,255,255,.15)">CONTACT</a>
  <a style="left:906px;width:132px">ABOUT</a>
</nav>
<section class="hero" role="img" aria-label="Sunset view of a harbour city with opera house and arch bridge reflected in the water">
  <svg style="left:102px" width="22" height="26" viewBox="0 0 22 26"><path d="M18 2L6 13l12 11" stroke="#fff" stroke-width="3" fill="none"/></svg>
  <svg style="left:1076px" width="22" height="26" viewBox="0 0 22 26"><path d="M4 2l12 11L4 24" stroke="#fff" stroke-width="3" fill="none"/></svg>
  <h1 class="hero-title">EDUCATIONAL, SAFE, CULTURALLY BRIGHTWATER LEARNING<br>TRIPS ENLIGHTENING AND FUN.</h1>
</section>
<section class="features">
  <div class="feature" style="left:142px">
    <div class="halo"><div class="badge navy" role="img" aria-label="Graduation cap icon"></div></div>
    <h3 class="highlight">Educational And Cultural</h3>
  </div>
  <div class="feature" style="left:467px">
    <div class="halo"><div class="badge gold">
      <svg width="58" height="66" viewBox="0 0 58 66"><path d="M29 3L53 12v20c0 16-11 26-24 31C16 58 5 48 5 32V12z" fill="#fff"/><path d="M17 33l9 9 16-18" stroke="var(--gold)" stroke-width="7" fill="none" stroke-linecap="round" stroke-linejoin="round"/></svg>
    </div></div>
    <h3>Safe And Secure</h3>
  </div>
  <div class="feature" style="left:794px">
    <div class="halo"><div class="badge gold" role="img" aria-label="Airplane and globe icon"></div></div>
    <h3>Travel insurance</h3>
  </div>
</section>
<div class="divider"></div>
<section class="about">
  <h2><span class="gold">ABOUT</span> BRIGHTWATER <span class="gold">LEARNING</span> TRIPS</h2>
  <div class="ornament"><span></span></div>
  <p class="lead">At Brightwater Learning Trips We Are Passionate About Educational Travel And Opportunities For Students To Gain Academic And Cultural Understanding Of Australia.</p>
  <p class="body">14 day premium cultural and educational tours to Australian cities. Educational, safe, culturally enlightening and fun. Learn about educational institutions, history, sports, laws and customs, food and culture while improving your English.</p>
  <a class="read-more">READ MORE</a>
</section>
<footer class="footer">
  <p>© 2015 &nbsp;BRIGHTWATER LEARNING TRIPS. All Rights Reserved.</p>
  <div class="social"><span></span><span></span><span></span></div>
</footer>
</body>
</html>
```